Vardel coatings banner

Banner same size Brisk Hallways advert banner
of previous one Brisk Hallways advert banner 215cm x 1055cm
but for a paint company, called Vardel Coatings.
I want the concept to be similar to the attached, i want to put some real drum paint in front of the banner concept to look in Harmony with your concept on the banner.
The company is specialized in producing and painting houses and offices indoor and outdoor and applying epoxy on floors..

```html
<!DOCTYPE html>
<html lang="en">
<head>
<meta charset="utf-8">
<title>Vardel Coatings banner</title>
<link rel="stylesheet" href="https://fonts.googleapis.com/css2?family=IBM+Plex+Sans:wght@600;700&display=swap">
<style>
  :root {
    --brand-blue: #2f6fae;
    --brand-navy: #245f99;
    --paint-blue: #5fb2e8;
    --background: #ffffff;
  }
  * { margin: 0; padding: 0; box-sizing: border-box; }
  html, body { width: 1200px; height: 245px; overflow: hidden; background: var(--background); }
  .banner {
    position: relative;
    width: 1200px;
    height: 245px;
    background: var(--background);
    overflow: hidden;
    font-family: "IBM Plex Sans", Arial, sans-serif;
  }
  .paint-spill {
    position: absolute;
    top: 0;
    height: 245px;
  }
  .paint-spill--left {
    left: 0;
    width: 403px;
    background: linear-gradient(to right, var(--paint-blue) 0%, var(--paint-blue) 35%, rgba(95,178,232,0) 100%);
  }
  .paint-spill--right {
    right: 0;
    width: 450px;
    background: linear-gradient(to left, var(--paint-blue) 0%, var(--paint-blue) 35%, rgba(95,178,232,0) 100%);
  }
  .brand {
    position: absolute;
    top: 28px;
    left: 482px;
    display: flex;
    align-items: center;
    gap: 12px;
  }
  .brand-dot {
    width: 56px;
    height: 56px;
    border-radius: 50%;
    background: var(--brand-navy);
  }
  .brand-name {
    color: var(--brand-blue);
    font-weight: 600;
    font-size: 24px;
    line-height: 24px;
    letter-spacing: 0.3px;
    text-transform: uppercase;
  }
  .headline {
    position: absolute;
    top: 96px;
    left: 366px;
    width: 400px;
    text-align: center;
    color: var(--brand-blue);
    font-weight: 700;
    font-size: 26px;
    line-height: 32px;
  }
</style>
</head>
<body>
  <main class="banner">
    <div class="paint-spill paint-spill--left" role="img" aria-label="Tipped paint drum spilling bright blue paint"></div>
    <div class="paint-spill paint-spill--right" role="img" aria-label="Tipped paint drum spilling bright blue paint"></div>

    <div class="brand">
      <span class="brand-dot" aria-hidden="true"></span>
      <span class="brand-name">Vardel<br>Coatings</span>
    </div>

    <h1 class="headline">We paint houses and<br>offices indoor and outdoor<br>and apply epoxy on<br>the floor.</h1>
  </main>
</body>
</html>
```